Website Redesign for Non-Profit Ministry & Church

NOTE: Please do not contact me privately — all private inquiries will be ignored.

Individuals seeking spiritual healing, community connection, ministry support and journal-based encounters.

Description of What’s Needed

We need a clean, fresh, inviting website that encourages engagement and connection. The site should feel warm and accessible, draw people in, and clearly present who we are, what we offer, and how visitors can participate. The layout should be straightforward, with well-structured pages (no overlapping objects, minimal layering complexity) and easy to navigate. Use only Google Fonts. All stock photos must be sourced from royalty-free sites and include proper attribution. We will not include a search feature.

Pages to Create
1. Home Page – impactful hero area, clear call-to-action, visual story of ministry, giving/gathering invitation.
2. About Us – vision, mission, leadership, testimonies, history.
3. Meetings & Events – upcoming gatherings, schedule, how to attend, sign-up or interest form.
4. Encounter: “Sketching Toward Dawn” (book) – dedicated page for the book, overview, purchase link or details, journal prompts, imagery.
5. Mending Halls / Ministry – explain ministry offerings, invite participation, testimonials or case-studies.
6. Live Stream & Links Page – page listing links for YouTube live stream, other platforms, archive links; simple layout.

Colour & Branding

Use colours that blend with our existing logo (attached). The palette should feel contemporary, welcoming, and aligned with ministry themes of restoration, healing and love. Ensure text, button and link colours maintain good contrast for accessibility.

Existing Content & Reference

Please gather available content from our current website in the attachment here for text, images and structure for reuse.

Imagery Guidelines

– Use original photos from our Facebook page or Google Location listing for building or people images when available.
– If generic images are used, ensure they depict appropriate ministry-related buildings or people (community, warm gathering) — avoid generic unrelated stock imagery.
– All photos must be royalty-free or have proper licensing and attribution.
– No overlapping objects or visual clutter; clean layouts with defined sections.

Additional Notes

– Integration: We currently utilise MailChimp for email communication; the design should include a connection/invite to subscribe (via MailChimp) but no blog page is required at this time.
– Payment/Giving: We accept PayPal and already have a giving portal; include clear donation/give buttons or calls-to-action linking to existing giving systems.
– No search function to be included.
– Layouts should avoid complex layering or overlapping elements—designers should work with distinct content blocks, clear visual hierarchy, and straightforward mobile-friendly structure.

Target Market(s)

Industry/Entity Type

Church/Religious institution

Number of Pages Required

5+ page

Requirements
Should not have
• search bar

```html
<!DOCTYPE html>
<html lang="en">
<head>
<meta charset="utf-8">
<title>Held Mended Whole — Home</title>
<link href="https://fonts.googleapis.com/css2?family=Montserrat:wght@400;500;600;700;800&family=Open+Sans:wght@400;600&display=swap" rel="stylesheet">
<style>
:root{
  --teal:#17a58e;
  --purple:#5a2a88;
  --ink:#222;
  --muted:#555;
  --paper:#fff;
  --mist:#ececec;
  --footer:#242424;
}
*{margin:0;padding:0;box-sizing:border-box}
html,body{width:1200px;height:3632px;overflow:hidden}
body{font-family:"Open Sans",Arial,sans-serif;color:var(--ink);background:var(--paper);position:relative}
h1,h2,h3,.brand,.nav,.btn{font-family:Montserrat,Arial,sans-serif}
.btn{display:inline-block;color:#fff;font-weight:600;font-size:16px;padding:14px 34px;border-radius:30px;text-decoration:none}
.btn-teal{background:var(--teal)}
.btn-purple{background:var(--purple)}

/* header */
.site-header{height:100px;display:flex;align-items:center;padding:0 60px;justify-content:space-between}
.brand{display:flex;align-items:center;gap:12px;font-weight:700;font-size:24px;color:var(--teal);line-height:1.05;width:200px}
.brand-dot{width:22px;height:22px;border-radius:50%;background:var(--teal);flex:none}
.nav{display:flex;gap:38px;font-size:15px;font-weight:600}
.nav a{color:var(--ink);text-decoration:none;padding-bottom:6px}
.nav a.active{color:var(--purple);border-bottom:3px solid var(--teal)}

/* hero */
.hero{height:480px;position:relative;background:linear-gradient(180deg,#5b5f66 0%,#3b4048 55%,#2a2f36 100%);display:flex;flex-direction:column;align-items:center;justify-content:center;text-align:center;color:#fff}
.hero h1{font-size:58px;font-weight:800;line-height:1.12;margin-top:40px}
.hero .btn{margin-top:26px}
.hero-dots{position:absolute;bottom:26px;display:flex;gap:10px}
.hero-dots span{width:10px;height:10px;border-radius:50%;background:rgba(255,255,255,.55)}
.hero-dots span.on{background:#fff}

/* story */
.story{height:600px;display:flex;align-items:center;padding:100px 70px 0;gap:60px}
.photo{border-radius:0 60px 0 60px}
.story .photo{width:420px;height:290px;background:linear-gradient(135deg,#8a96a6,#4b5563 60%,#b9c2cc);border-bottom:6px solid var(--teal);border-left:6px solid var(--teal);flex:none}
.section-title{font-size:40px;font-weight:700;color:var(--ink);line-height:1.15}
.section-title em{font-style:normal;color:var(--teal)}
.story p,.gather p{font-size:14.5px;line-height:1.6;color:var(--muted);margin-top:16px}
.story .btn,.gather .btn{margin-top:22px}

/* mission */
.mission{height:500px;position:relative;color:#fff;text-align:center}
.mission svg{position:absolute;inset:0}
.mission .inner{position:relative;padding-top:175px;width:820px;margin:0 auto}
.mission h2{font-size:40px;font-weight:700}
.mission p{font-size:14.5px;line-height:1.65;margin-top:18px;opacity:.92}

/* gathering */
.gather{height:560px;display:flex;align-items:center;padding:40px 70px 0;gap:60px}
.gather .text{width:500px;flex:none}
.gather .photo{width:500px;height:300px;flex:none;background:linear-gradient(135deg,#b7a58d,#6d6456 55%,#3f3a33);border-top:6px solid var(--teal);border-right:6px solid var(--teal)}

/* newsletter */
.newsletter-wrap{height:370px;position:relative}
.newsletter{position:absolute;left:0;right:0;top:20px;height:350px;background:var(--mist);display:flex;align-items:center;padding:0 70px;gap:60px}
.newsletter .intro{width:440px;flex:none}
.newsletter h2{font-size:40px;font-weight:700;color:var(--ink)}
.newsletter h2 em{font-style:normal;color:var(--teal)}
.newsletter p{font-size:14px;color:var(--muted);margin-top:8px}
.signup{width:580px;display:grid;grid-template-columns:1fr 1fr;gap:16px}
.signup .field{background:#fff;border-radius:24px;height:46px;padding:0 20px;display:flex;align-items:center;font-size:14px;color:#888}
.signup .btn{grid-column:1/3;text-align:center;padding:14px 0}

/* blog */
.blog{height:730px;padding-top:50px;text-align:center}
.posts{display:flex;justify-content:center;gap:50px;margin-top:46px}
.post{width:320px}
.post .thumb{height:200px;border-radius:0 50px 0 50px}
.thumb-cross{background:linear-gradient(180deg,#23394f,#b05a3a 70%,#3a2a22)}
.thumb-road{background:linear-gradient(180deg,#6fa0d0,#e3c17a 55%,#6b7b4a)}
.thumb-sunset{background:linear-gradient(180deg,#f2a23c,#e36b2c 60%,#5a3020)}
.post h3{font-size:21px;font-weight:700;color:var(--teal);margin-top:22px;line-height:1.25}
.post p{font-size:13.5px;line-height:1.55;color:var(--muted);margin-top:12px}
.blog .btn{margin-top:48px}

/* footer */
.site-footer{position:absolute;left:0;right:0;bottom:0;height:292px;background:var(--footer);color:#ccc;display:flex;padding:60px 70px 0}
.site-footer .col{font-size:14px;line-height:1.75}
.site-footer h3{color:#fff;font-size:19px;font-weight:700;margin-bottom:12px}
.site-footer .brand{width:auto}
.copy{font-size:12px;color:#aaa;margin-top:18px;line-height:1.5}
.col-brand{width:380px}.col-links{width:250px}.col-contact{width:330px}
.socials{display:flex;gap:14px;margin-top:4px}
.socials span{width:22px;height:22px;border-radius:50%;background:var(--teal)}
</style>
</head>
<body>

<header class="site-header">
  <div class="brand"><span class="brand-dot"></span><span>Held Mended Whole</span></div>
  <nav class="nav">
    <a class="active" href="#">Home</a>
    <a href="#">About Us</a>
    <a href="#">Meetings &amp; Events</a>
    <a href="#">Sketching Toward Dawn</a>
    <a href="#">Mending Halls</a>
    <a href="#">Live Stream</a>
  </nav>
</header>

<section class="hero" role="img" aria-label="Congregation gathered in a sanctuary while a minister speaks at the front">
  <h1>Welcome to<br>Held Mended Whole</h1>
  <a class="btn btn-teal" href="#">Learn More</a>
  <div class="hero-dots"><span class="on"></span><span></span><span></span></div>
</section>

<section class="story">
  <div class="photo" role="img" aria-label="Minister preaching at a lectern beside a stained glass window"></div>
  <div class="text">
    <h2 class="section-title">Story About <em>Our<br>Ministry</em></h2>
    <p>The Mending Halls of Held Mended Whole is a ministry centered in showing God's love as Christians from different backgrounds and experiences come together in unity to pray for the sick. We believe in God's power to heal.</p>
    <p>We are members of the Global Circle of Mending Halls, which began in 2006 in Alder Creek, Montana by Rev. Dale Fenwick. More than 800 mending rooms now open across many countries.</p>
    <a class="btn btn-purple" href="#">Learn More</a>
  </div>
</section>

<section class="mission">
  <svg width="1200" height="500" viewBox="0 0 1200 500" aria-hidden="true">
    <defs>
      <linearGradient id="forest" x1="0" y1="0" x2="0" y2="1">
        <stop offset="0" stop-color="#0f4a38"/><stop offset="1" stop-color="#06241b"/>
      </linearGradient>
    </defs>
    <path d="M0 60 C300 0 700 120 1200 40 L1200 460 C800 520 400 410 0 480 Z" fill="url(#forest)"/>
    <path d="M0 60 C300 0 700 120 1200 40" fill="none" stroke="#17a58e" stroke-width="8"/>
    <path d="M0 480 C400 410 800 520 1200 460" fill="none" stroke="#17a58e" stroke-width="8"/>
  </svg>
  <div class="inner" role="img" aria-label="Worshippers raising hands in a dim hall">
    <h2>Our Mission &amp; Vision</h2>
    <p>Ministering God's presence by loving the broken, saving the lost, and healing the hurting through the demonstration of His love and power.</p>
    <p>Held Mended Whole is here to activate, proclaim and teach the love of the Father through Jesus with the guidance of the Holy Spirit.</p>
  </div>
</section>

<section class="gather">
  <div class="text">
    <h2 class="section-title">Gathering <em>Invitation</em></h2>
    <p>If you are hosting an event at your church or ministry, or you prayerfully seek the Lord for guidance, we share these thoughts regarding Ruth &amp; Daniel Ashby and their ministry.</p>
    <p>I have served in church leadership with Ruth and Daniel for several years, and I do not know of a more balanced and powerful ministry of miracles and healings. They are activators not only of supernatural demonstrations but of supernatural compassion.</p>
    <a class="btn btn-purple" href="#">Learn More</a>
  </div>
  <div class="photo" role="img" aria-label="Ministry team praying together at the front of a church"></div>
</section>

<section class="newsletter-wrap">
  <div class="newsletter">
    <div class="intro">
      <h2>Join Our <em>Newsletter</em></h2>
      <p>Signup today for free and be the first to get notified on new updates.</p>
    </div>
    <form class="signup">
      <div class="field">Name</div>
      <div class="field">Email Address</div>
      <a class="btn btn-purple" href="#">Subscribe Now</a>
    </form>
  </div>
</section>

<section class="blog">
  <h2 class="section-title">HMW <em>Blog Posts</em></h2>
  <div class="posts">
    <article class="post">
      <div class="thumb thumb-cross" role="img" aria-label="Cross silhouetted against an evening sky"></div>
      <h3>Nothing is incurable<br>for God</h3>
      <p>My healings have come in a variety of ways. Several of these healings have been for incurable diseases.</p>
    </article>
    <article class="post">
      <div class="thumb thumb-road" role="img" aria-label="Rainbow arching over an open country road"></div>
      <h3>Healing amidst the<br>car accident</h3>
      <p>It was a typical Friday afternoon on May 5, 2013. I was on my way to a nearby town to meet a friend.</p>
    </article>
    <article class="post">
      <div class="thumb thumb-sunset" role="img" aria-label="Bird flying across a golden sunset"></div>
      <h3>Healing - where and how<br>can it happen?</h3>
      <p>That may sound like a complicated question but it is very simple. God is omnipotent. That means His power has no limits.</p>
    </article>
  </div>
  <a class="btn btn-purple" href="#">View All Blog Posts</a>
</section>

<footer class="site-footer">
  <div class="col col-brand">
    <div class="brand"><span class="brand-dot"></span><span>Held Mended Whole</span></div>
    <p class="copy">Copyright © 2025 Held Mended Whole.<br>All rights reserved.</p>
  </div>
  <div class="col col-links">
    <h3>Quick Links</h3>
    Home<br>About Us<br>Meetings &amp; Events<br>Sketching Toward Dawn<br>Mending Halls<br>Live Stream
  </div>
  <div class="col col-contact">
    <h3>Contact Info</h3>
    4120 Willow Bend Lane,<br>Cedar Falls, United States,<br>Iowa<br>+1 555 014 2290<br>hello@heldmendedwhole.org
  </div>
  <div class="col">
    <h3>Follow Us</h3>
    <div class="socials"><span></span><span></span><span></span><span></span><span></span></div>
  </div>
</footer>

</body>
</html>
```